Marlow Realty Real Estate Brokerage Recruiting Flyer

We are a real estate brokerage looking to hire more real estate agents. We need to list everything we have to offer as a company so real estate agents will join our company. this is our company website: www.Marlowrealty.example .

100% COMMISSION NO MONTHLY FEE
$450 Flat Transaction FEE

What We Offer:
24/7 Office Access
Free E & O Insurance for 1st Year
Free Online CE and PLE
Free 1,000 Business Cards
Free Professional Social Media Marketing
Free Printing, Scanning, and Copies
Free Buyer and Seller Presentation Packages
Free Filquay Cloud Based Document Management Access
Access to our Internal Brokerage Forum
Company Profit Sharing!
Private Offices Available to Rent

*Lead Generation Software with over 3,000 Leads
*10 Leads to Start
* Free Personal CRM and Website
*Restrictions and Rules apply

Company Address:
4817 Amberfield Road
Suite 512
Fairfax, VA 22194
Phone: 703-555-0147
email: info@marlowrealty.example

Target Market(s)

Real Estate Agents

Industry/Entity Type

Real Estate

Colors
0555a3
ffffff

Requirements
Must have
• 100% COMMISSION NO MONTHLY FEE
$450 Flat Transaction FEE

What We Offer:
24/7 Office Access
Free Online CE and PLE
Free 1,000 Business Cards
Company Profit Sharing!

*10 Leads to Start

Company Address:
4817 Amberfield Road
Suite 512
Fairfax, VA 22194
Phone: 703-555-0147

```html
<!DOCTYPE html>
<html lang="en">
<head>
<meta charset="utf-8">
<title>Marlow Realty – Come Grow With Us</title>
<link rel="stylesheet" href="https://fonts.googleapis.com/css2?family=Montserrat:wght@400;500;600;700;800;900&display=swap">
<style>
  :root {
    --brand-blue: #0555a3;
    --deep-blue: #0b57a4;
    --teal: #1a9e9e;
    --light-teal: #abdde4;
    --panel-bg: #f2f7f7;
    --skyline: #b7b9de;
    --highlight: #ffeb00;
    --ink: #111111;
    --white: #ffffff;
    --rule: #3d4f9a;
  }
  * { box-sizing: border-box; margin: 0; padding: 0; }
  html, body { width: 849px; height: 1200px; overflow: hidden; background: var(--white); }
  body { font-family: "Montserrat", Arial, sans-serif; color: var(--ink); }
  .flyer { position: relative; width: 849px; height: 1200px; overflow: hidden; }
  .abs { position: absolute; }

  .header-band { left: 48px; top: 50px; width: 754px; height: 126px; }
  .hero-photo {
    left: 48px; top: 176px; width: 754px; height: 285px;
    background: linear-gradient(180deg, #c9cfd4 0%, #9aa3aa 35%, #3b4455 70%, #232a3a 100%);
  }
  .hero-rule { left: 48px; top: 461px; width: 754px; height: 10px; background: var(--brand-blue); }

  .offer-panel { left: 48px; top: 490px; width: 754px; height: 532px; background: var(--panel-bg); }

  .headline { left: 48px; top: 482px; width: 754px; height: 140px; }

  .offer-tab {
    left: 48px; top: 625px; width: 298px; height: 36px; background: var(--light-teal);
    color: var(--brand-blue); font-weight: 900; font-size: 25px; letter-spacing: -0.5px;
    padding: 4px 0 0 17px; line-height: 30px;
  }
  .tab-rule { left: 346px; top: 642px; width: 430px; height: 1px; background: var(--rule); }

  .benefits { list-style: none; font-size: 15px; line-height: 19px; color: #1f1f1f; }
  .benefits li { position: absolute; padding-left: 12px; white-space: nowrap; }
  .benefits li::before { content: "•"; position: absolute; left: 0; top: 0; font-weight: 700; }
  .benefits b { font-weight: 700; }
  .tone-teal { color: var(--teal); }
  .tone-blue { color: var(--brand-blue); }
  .list-left li { left: 65px; }
  .list-right li { left: 427px; }
  .column-rule { left: 407px; top: 674px; width: 1px; height: 143px; background: var(--rule); }
  .section-rule { left: 72px; top: 833px; width: 706px; height: 1px; background: var(--rule); }

  .skyline-area {
    left: 52px; top: 862px; width: 746px; height: 150px;
    background: linear-gradient(180deg, rgba(183,185,222,0.75), rgba(183,185,222,0.35));
  }

  .perk {
    width: 160px; height: 160px; border-radius: 50%; background: var(--brand-blue);
    box-shadow: 0 4px 8px rgba(0,0,0,0.25);
    display: flex; flex-direction: column; align-items: center; justify-content: center;
    color: var(--white); font-weight: 700; text-align: center; line-height: 1;
  }
  .perk .line { font-size: 17.5px; line-height: 18.5px; }
  .perk .yellow { color: var(--highlight); }
  .perk-leads { left: 133px; top: 847px; }
  .perk-leads .big { font-size: 44px; letter-spacing: -2px; line-height: 40px; }
  .perk-start { left: 345px; top: 847px; }
  .perk-start .big { font-size: 84px; letter-spacing: -5px; line-height: 70px; position: relative; }
  .perk-start .star { position: absolute; left: -12px; top: 2px; font-size: 16px; letter-spacing: 0; color: var(--white); }
  .perk-crm { left: 557px; top: 847px; }
  .perk-crm .mid { font-size: 29px; line-height: 28px; }

  .footer-art { left: 48px; top: 1020px; width: 754px; height: 108px; }
  .footnote { left: 64px; top: 1021px; font-size: 9px; color: #333; z-index: 2; }
  .contact { left: 65px; top: 1045px; color: var(--white); font-weight: 600; font-size: 16px; line-height: 19px; white-space: nowrap; }
  .licensed { left: 311px; top: 1107px; color: var(--white); font-size: 9px; font-weight: 500; letter-spacing: 0.5px; }
  .brand-mark { left: 598px; top: 1062px; display: flex; align-items: center; gap: 8px; }
  .brand-mark .square { width: 26px; height: 26px; background: var(--brand-blue); }
  .brand-mark .name { font-size: 22px; font-weight: 500; color: var(--brand-blue); white-space: nowrap; }

  .social-rule { top: 1150px; height: 1px; background: #7a86b4; }
  .social-rule.left { left: 46px; width: 261px; }
  .social-rule.right { left: 532px; width: 270px; }
  .social-dot { top: 1138px; width: 25px; height: 25px; border-radius: 50%; background: var(--brand-blue); }
  .handle { left: 405px; top: 1142px; font-size: 11.5px; font-weight: 700; color: #1a1a1a; }
</style>
</head>
<body>
<div class="flyer">

  <svg class="abs header-band" viewBox="0 0 754 126">
    <rect width="754" height="108" fill="var(--brand-blue)"/>
    <rect y="108" width="754" height="18" fill="var(--light-teal)"/>
    <polygon points="280,0 500,0 370,126 150,126" fill="var(--light-teal)"/>
    <polygon points="150,126 170,108 190,126" fill="var(--teal)"/>
    <polygon points="570,0 700,0 560,126 430,126" fill="var(--light-teal)"/>
    <polygon points="570,0 620,0 460,126 440,126" fill="var(--teal)"/>
    <text x="377" y="77" text-anchor="middle" textLength="640" lengthAdjust="spacingAndGlyphs"
          font-family="Montserrat, Arial, sans-serif" font-weight="900" font-size="58"
          fill="var(--brand-blue)" stroke="var(--white)" stroke-width="8" stroke-linejoin="round"
          paint-order="stroke">COME GROW WITH US!</text>
  </svg>

  <div class="abs hero-photo" role="img" aria-label="Team photo of eight real estate agents in business attire standing with arms crossed in a bright modern office lobby"></div>
  <div class="abs hero-rule"></div>

  <div class="abs offer-panel"></div>

  <svg class="abs headline" viewBox="0 0 754 140">
    <text x="377" y="45" text-anchor="middle" textLength="563" lengthAdjust="spacingAndGlyphs"
          font-family="Montserrat, Arial, sans-serif" font-weight="700" font-size="56" fill="var(--brand-blue)">100% COMMISSION</text>
    <text x="377" y="96" text-anchor="middle" textLength="540" lengthAdjust="spacingAndGlyphs"
          font-family="Montserrat, Arial, sans-serif" font-weight="700" font-size="56" fill="var(--brand-blue)">NO MONTHLY FEE</text>
    <text x="377" y="132" text-anchor="middle" textLength="460" lengthAdjust="spacingAndGlyphs"
          font-family="Montserrat, Arial, sans-serif" font-weight="700" font-size="32" fill="var(--ink)">$450 Flat Transaction FEE</text>
  </svg>

  <div class="abs offer-tab">WHAT WE OFFER:</div>
  <div class="abs tab-rule"></div>

  <ul class="benefits list-left">
    <li style="top:670px"><b class="tone-teal">24/7</b> Office Access</li>
    <li style="top:694px"><b class="tone-blue">FREE</b> E&amp;O Insurance for 1st Year</li>
    <li style="top:719px"><b class="tone-teal">FREE</b> Online CE and PLE</li>
    <li style="top:743px"><b class="tone-blue">FREE</b> 1,000 Business Cards</li>
    <li style="top:767px"><b class="tone-teal">FREE</b> Professional Social Media Marketing</li>
    <li style="top:792px"><b class="tone-blue">FREE</b> Printing, Scanning, and Copies</li>
  </ul>
  <div class="abs column-rule"></div>
  <ul class="benefits list-right">
    <li style="top:669px"><b class="tone-teal">FREE</b> Buyer and Seller Presentation Packages</li>
    <li style="top:694px"><b class="tone-blue">FREE</b> Filquay Cloud Based Document<br>Management Access</li>
    <li style="top:739px"><b class="tone-teal">ACCESS</b> to our Internal Brokerage Forum</li>
    <li style="top:765px"><b class="tone-blue">COMPANY</b> Profit Sharing!</li>
    <li style="top:793px"><b class="tone-teal">PRIVATE</b> Offices Available to Rent</li>
  </ul>
  <div class="abs section-rule"></div>

  <div class="abs skyline-area" role="img" aria-label="Soft lavender silhouette of neighborhood houses behind the perk badges"></div>

  <div class="abs perk perk-leads">
    <span class="line">*Lead</span>
    <span class="line">Generation</span>
    <span class="line">Software</span>
    <span class="line">with over</span>
    <span class="big yellow">3,000</span>
    <span class="line yellow">Leads</span>
  </div>
  <div class="abs perk perk-start">
    <span class="big yellow"><span class="star">*</span>10</span>
    <span class="line yellow">Leads</span>
    <span class="line">to start</span>
  </div>
  <div class="abs perk perk-crm">
    <span class="line">*Free</span>
    <span class="line">Personal</span>
    <span><span class="mid yellow">CRM</span> <span class="line">and</span></span>
    <span class="mid yellow">Website</span>
  </div>

  <svg class="abs footer-art" viewBox="0 0 754 108">
    <rect x="0" y="0" width="754" height="108" fill="var(--light-teal)"/>
    <rect x="0" y="0" width="400" height="17" fill="var(--panel-bg)"/>
    <polygon points="0,17 428,17 533,108 0,108" fill="var(--brand-blue)"/>
    <polygon points="390,17 408,2 428,17" fill="var(--teal)"/>
  </svg>

  <div class="abs footnote">*Restrictions and Rules apply</div>

  <div class="abs contact">
    4817 Amberfield Road, Suite 512, Fairfax, VA 22194<br>
    Phone: 703-555-0147<br>
    email: info@marlowrealty.example<br>
    www.Marlowrealty.example
  </div>
  <div class="abs licensed">LICENSED IN D.C., MARYLAND, AND VIRGINIA</div>

  <div class="abs brand-mark">
    <span class="square"></span>
    <span class="name">Marlow Realty</span>
  </div>

  <div class="abs social-rule left"></div>
  <div class="abs social-rule right"></div>
  <span class="abs social-dot" style="left:315px"></span>
  <span class="abs social-dot" style="left:345px"></span>
  <span class="abs social-dot" style="left:374px"></span>
  <div class="abs handle">@MarlowRealtyDMW</div>

</div>
</body>
</html>
```